POSTER ARTWORK FOR FILM FESTIVAL

The Mellowbrook Cinema Gala, an international film event of 22 years and counting, is looking for inspiring art for its 2020 poster. In particular, we are hoping to find a central image that would relay the theme of "vision". Some graphical elements we would like the design to convey -- eye chart, 2020 vision, film elements, the words "MELLOWBROOK CINEMA GALA" in some prominent fashion as well as the festival dates -- "March 27 - April 5th." It could also have mysterious symbols and other words (perhaps as part of the eye chart) -- "2020, diversity, inclusion, vision, focus, clarity". Other design inspirations - the graphical work of Lionel Fawcett, a writer and book illustrator (specifically his whimsical alphabet). Feel free to be creative with this project! More about us --- http://mellowbrookcinemagala.com
For printing, we would need a hi-res, 300DPI file that would look good if printed in at least 24"x36" size. Ideally, you should output a vector file. The image should be vertical.
NOTE: you can't use the Fawcett imagery directly as it's copyrighted. We are looking for something inspired by it (esp lettering).

```html
<!DOCTYPE html>
<html lang="en">
<head>
<meta charset="utf-8">
<title>The Mellowbrook Cinema Gala 2020 Poster</title>
<link href="https://fonts.googleapis.com/css2?family=Nunito:wght@800;900&display=swap" rel="stylesheet">
<style>
  :root {
    --backdrop: #5f5f5f;
    --poster-black: #000000;
    --pattern-tone: #3a3a3a;
    --magenta: #ff1aff;
    --cyan: #29abe2;
  }
  * { margin: 0; padding: 0; box-sizing: border-box; }
  html, body { width: 1200px; height: 996px; overflow: hidden; background: var(--backdrop); }
  .canvas { position: relative; width: 1200px; height: 996px; font-family: "Nunito", "Arial Rounded MT Bold", sans-serif; }
  .poster { position: absolute; left: 327px; top: 89px; width: 559px; height: 838px; background: var(--poster-black); overflow: hidden; }
  .poster-pattern { position: absolute; inset: 0; background:
      radial-gradient(circle at 20% 15%, var(--pattern-tone) 0, transparent 18%),
      radial-gradient(circle at 78% 18%, var(--pattern-tone) 0, transparent 16%),
      radial-gradient(circle at 15% 70%, var(--pattern-tone) 0, transparent 15%),
      radial-gradient(circle at 82% 88%, var(--pattern-tone) 0, transparent 17%),
      radial-gradient(circle at 40% 90%, #262626 0, transparent 20%),
      var(--poster-black); }
  .chart-frame { position: absolute; left: 112px; top: 225px; width: 344px; height: 368px; background: var(--poster-black); border: 2px solid var(--magenta); }
  .chart-row { position: absolute; left: 20px; right: 20px; display: flex; justify-content: space-between; line-height: 1; font-weight: 900; }
  .solid { color: var(--magenta); }
  .outline { color: transparent; -webkit-text-stroke: 2.4px var(--cyan); }
  .row-title { top: 22px; font-size: 118px; }
  .row-name-1 { top: 124px; font-size: 58px; }
  .row-name-1.outline { -webkit-text-stroke-width: 3px; }
  .row-name-2 { top: 199px; font-size: 32px; }
  .row-name-3 { top: 245px; font-size: 22px; }
  .row-dates { top: 283px; font-size: 15px; color: var(--cyan); }
  .row-year { top: 309px; font-size: 15px; color: var(--magenta); }
  .row-name-2 span.outline { -webkit-text-stroke-width: 2px; }
</style>
</head>
<body>
<div class="canvas">
  <section class="poster">
    <div class="poster-pattern" role="img" aria-label="Scattered pattern of grey eyeballs and film reels on black"></div>
    <div class="chart-frame">
      <div class="chart-row row-title solid"><span>T</span><span>H</span><span>E</span></div>
      <div class="chart-row row-name-1 outline"><span>M</span><span>E</span><span>L</span><span>L</span><span>O</span><span>W</span><span>-</span></div>
      <div class="chart-row row-name-2"><span class="outline">B</span><span class="outline">R</span><span class="outline">O</span><span class="outline">O</span><span class="outline">K</span><span class="solid">C</span><span class="solid">I</span><span class="solid">N</span><span class="solid">E</span><span class="solid">M</span><span class="solid">A</span></div>
      <div class="chart-row row-name-3 solid"><span>G</span><span>A</span><span>L</span><span>A</span></div>
      <div class="chart-row row-dates"><span>M</span><span>A</span><span>R</span><span>C</span><span>H</span><span>2</span><span>7</span><span>-</span><span>A</span><span>P</span><span>R</span><span>I</span><span>L</span><span>5</span><span>T</span><span>H</span></div>
      <div class="chart-row row-year"><span>2</span><span>0</span><span>2</span><span>0</span></div>
    </div>
  </section>
</div>
</body>
</html>
```